New Slide Master Template for PPT

I need a new Slide Master / Template for PPT presentations. Our company does Cloud Management / Network Management systems that are used to manage devices connected to the internet. Those devices can be things like Wireless Access Points, DSL modems, Cable modems, Gateways, Routers, Switches, and the equipment that is in the internet such as Brevok, Talsome, or Ormavin-Dusk equipment.
What our management system does is connect/communicate with all these different devices to be able to get information from the devices such as throughput performance, wireless coverage, failures conditions, firmware versions, and any other information which is used to manage, control, or troubleshoot those devices for the equipment companies or internet service providers who have provided them to their end customers for internet service.
The new Slide Master / Template for PowerPoint needs to do to the following;
1. be fresh and current in design
2. have a nice looking font that works for both print and presentation on small screens (laptops) as well as big screen (large group presentations)
3. not consume too many MegaBytes when saved as a file. Many email servers have limits on the size of files which can be transferred as an attachment. Most are either 5 or 10 MB limits. I do not want to have to zip the file to get it under such size restrictions.
4. the colors in the "Quorvian" logo are the company colors (the orange and blue), those should be incorporated in some form in the Slide Master / Template.
5. the final design should communicate professionalism with a modern look and feel.
6. once done the attached (old version of presentation) should be transferred over using the new Slide Master / Template and new fonts.
NOTE: I am not seeing how to attach my current PPT file to this project. Please email me at tobias@fernpathsystems.example and I will send you the current presentation which needs to be updated as described above.
Updates
Target Market(s)
Networking equipment manufacturers like Brevok, Pylorn, Ormavin-Dusk, VoxTe, etc.
Industry/Entity Type
Internet
Look and feel
Each slider illustrates characteristics of the customer's brand and the style your logo design should communicate.

```html
<!DOCTYPE html>
<html lang="en">
<head>
<meta charset="utf-8">
<title>Quorvian – Slide Master Proposal</title>
<link rel="stylesheet" href="https://fonts.googleapis.com/css2?family=Graduate&family=Arimo:wght@400;700&family=EB+Garamond:wght@400&display=swap">
<style>
  :root{
    --orange:#f7ad3c;
    --blue:#1a64b4;
    --ink:#2b2b2b;
    --body:#555;
    --slide-bg:#f6f6f6;
    --frame:#c9c9c9;
    --band:#2f2f2f;
    --black:#111;
    --white:#fff;
    --page:#ffffff;
  }
  *{box-sizing:border-box;margin:0;padding:0}
  html,body{width:1200px;height:900px;overflow:hidden;background:var(--page)}
  body{position:relative;font-family:"Arimo",Arial,sans-serif;color:var(--body)}

  .slide{position:absolute;background:var(--slide-bg);border:1px solid var(--frame);overflow:hidden}
  .slide::after{content:"";position:absolute;left:0;right:0;bottom:0;height:4px;background:var(--blue)}

  .badge{position:absolute;top:0;width:46px;height:62px}
  .badge text{font-family:"Arimo",Arial,sans-serif;font-weight:700;fill:var(--white)}

  .heading{position:absolute;font-family:"Graduate",serif;font-weight:400;line-height:1;text-transform:uppercase;white-space:nowrap}
  .heading .accent{color:var(--orange);display:block}
  .heading .main{color:var(--ink);display:block}

  .footer{position:absolute;left:0;right:0;background:var(--orange)}
  .url{position:absolute;left:3px;top:3px;bottom:3px;background:var(--black);color:var(--white);
       font:700 10px "Arimo",Arial,sans-serif;display:flex;align-items:center;padding:0 7px;white-space:nowrap}
  .url b{color:var(--blue);font-weight:700}
  .brand{position:absolute;right:3px;top:3px;bottom:3px;background:var(--black);color:var(--white);
         font:700 12px "Arimo",Arial,sans-serif;display:flex;align-items:center;gap:5px;padding:0 12px;white-space:nowrap}
  .brand i{width:12px;height:12px;border-radius:50%;background:var(--blue);display:block}

  .visual{position:absolute}

  /* cover */
  .cover{left:40px;top:198px;width:521px;height:293px;background:#f4f4f4}
  .cover .brand-top{position:absolute;right:14px;top:12px;display:flex;align-items:center;gap:5px;
                    font:700 13px "Arimo",Arial,sans-serif;color:var(--ink)}
  .cover .brand-top i{width:14px;height:14px;border-radius:50%;background:var(--blue);display:block}
  .cover .wifi{position:absolute;left:244px;top:40px}
  .cover h1{position:absolute;left:0;right:0;top:84px;text-align:center;font:400 33px "Graduate",serif;color:var(--ink);line-height:1;text-transform:uppercase}
  .cover h1 span{display:block;color:var(--orange);margin-top:10px}
  .cover .sub{position:absolute;left:0;right:0;top:180px;text-align:center;font:400 10px "EB Garamond",serif;color:var(--ink);letter-spacing:.5px}
  .cover .dark-band{position:absolute;left:0;right:0;top:225px;height:64px;background:var(--band)}
  .cover .dark-band .url{left:0;top:40px;bottom:auto;height:20px;background:none;font-size:11px}

  /* summary */
  .summary{left:40px;top:510px;width:521px;height:291px}
  .summary .lead{position:absolute;left:32px;top:88px;width:236px;font-size:9px;line-height:1.3}
  .summary .lead p+p{margin-top:14px}
  .summary .divider{position:absolute;left:278px;top:86px;width:1px;height:130px;background:var(--frame)}
  .summary .features{position:absolute;left:309px;top:88px;font-size:10px;line-height:1.22;color:#444}
  ul.bullets{list-style:none}
  ul.bullets li{position:relative;padding-left:13px}
  ul.bullets li::before{content:"";position:absolute;left:0;top:4px;width:5px;height:5px;background:var(--orange)}

  /* architecture */
  .architecture{left:665px;top:17px;width:438px;height:249px;background:#fff}

  /* planner */
  .planner{left:663px;top:275px;width:438px;height:246px;background:#fff}
  .planner .copy{position:absolute;left:28px;top:62px;width:195px;font-size:8.2px;line-height:1.3}
  .planner .copy p+p{margin-top:12px}
  .planner .divider{position:absolute;left:232px;top:62px;width:1px;height:130px;background:var(--frame)}
  .planner .note{position:absolute;left:242px;top:62px;font-size:8.2px}

  /* maps */
  .maps{left:656px;top:555px;width:449px;height:258px;background:#fff}
  .maps .notes{position:absolute;top:73px;font-size:8px;line-height:1.25}
  .maps .divider{position:absolute;left:211px;top:70px;width:1px;height:20px;background:var(--frame)}
</style>
</head>
<body>

<section class="slide cover">
  <svg class="badge" style="left:8px" viewBox="0 0 46 62" aria-hidden="true">
    <path d="M0 0H46V62L23 48L0 62Z" fill="var(--orange)"/>
    <text x="23" y="36" font-size="34" text-anchor="middle">*</text>
  </svg>
  <div class="brand-top"><i></i>Quorvian</div>
  <svg class="wifi" width="30" height="24" viewBox="0 0 30 24" aria-hidden="true">
    <g fill="none" stroke="var(--orange)" stroke-width="3" stroke-linecap="round">
      <path d="M3 9a17 17 0 0 1 24 0"/><path d="M8 14a10 10 0 0 1 14 0"/>
    </g>
    <circle cx="15" cy="19.5" r="2.5" fill="var(--orange)"/>
  </svg>
  <h1>WIFI Management<span>Systems</span></h1>
  <p class="sub">( BASED ON NEXAMANAGER )</p>
  <div class="dark-band"><div class="url">http://www.<b>quorvian</b>.example</div></div>
</section>

<section class="slide summary">
  <svg class="badge" style="left:9px" viewBox="0 0 46 62" aria-hidden="true">
    <path d="M0 0H46V62L23 48L0 62Z" fill="var(--orange)"/>
    <text x="23" y="38" font-size="30" text-anchor="middle">1</text>
  </svg>
  <h2 class="heading" style="left:64px;top:10px"><span class="accent" style="font-size:20px">WIFI Network</span><span class="main" style="font-size:19px;margin-top:5px">Management Summary</span></h2>
  <div class="lead">
    <p>Quorvian has successfully developed and deployed several large scale WiFi Network Management systems based on NexaManager for worldwide network device vendors.</p>
    <p>The WiFi management system based on NexaManager provides the IT manager the clarity and control to effectively manage mobile enterprise networks alone with the wired infrastructure from multiple vendors, through a web based centralized and easy-to-use interface</p>
  </div>
  <div class="divider"></div>
  <div class="features">
    <p>The main features are:</p>
    <ul class="bullets">
      <li>WiFi and LAN network discovery</li>
      <li>WiFi topology and heat maps</li>
      <li>WiFi planning tool</li>
      <li>Automated configuration</li>
      <li>AP Monitor and Dashboards</li>
      <li>Wireless client monitor</li>
      <li>Wireless Security</li>
      <li>Reports</li>
      <li>Network troubleshooting and diagnosis</li>
    </ul>
  </div>
  <div class="footer" style="top:249px;height:33px">
    <div class="url">http://www.<b>quorvian</b>.example</div>
    <div class="brand" style="width:118px"><i></i>Quorvian</div>
  </div>
</section>

<section class="slide architecture">
  <svg class="badge" style="left:9px" viewBox="0 0 46 62" aria-hidden="true">
    <path d="M0 0H46V62L23 48L0 62Z" fill="var(--orange)"/>
    <text x="23" y="34" font-size="28" text-anchor="middle">2</text>
  </svg>
  <h2 class="heading" style="left:63px;top:10px"><span class="accent" style="font-size:16px">WIFI Management :</span><span class="main" style="font-size:16px;margin-top:6px">Deployment Architecture</span></h2>
  <div class="visual" role="img" aria-label="Network deployment diagram: Java and web clients, management server, internet, probe server and access points"
       style="left:110px;top:64px;width:310px;height:142px;background:linear-gradient(135deg,#eef2f7,#dde6f1)"></div>
  <div class="footer" style="top:210px;height:31px">
    <div class="url">http://www.<b>quorvian</b>.example</div>
    <div class="brand" style="width:96px"><i></i>Quorvian</div>
  </div>
</section>

<section class="slide planner">
  <svg class="badge" style="left:9px" viewBox="0 0 46 62" aria-hidden="true">
    <path d="M0 0H46V62L23 48L0 62Z" fill="var(--orange)"/>
    <text x="23" y="34" font-size="28" text-anchor="middle">3</text>
  </svg>
  <h2 class="heading" style="left:60px;top:10px"><span class="accent" style="font-size:26px">WIFI Planner</span></h2>
  <div class="copy">
    <p>WiFi Planner can be integrated with WiFi network management systemsto support WiFi deployment.</p>
    <p>WiFi Planner accounts for floor maps, obstructions, access points configurations, antenna patterns and other variables to provide a reliable predictive map of WiFi signal and performance.</p>
    <p>It comes with auto WLAN modeling tool for superior predictive modeling to determine ideal quantity, placement and configuration of APs for optimal performance, security and compliance.</p>
  </div>
  <div class="divider"></div>
  <ul class="bullets note"><li>It is Web based and support all major browsers.</li></ul>
  <div class="visual" role="img" aria-label="WiFi planner screenshot with floor plan heat map"
       style="left:243px;top:78px;width:188px;height:116px;border:3px solid #333;background:radial-gradient(circle at 40% 35%,#f0b14a,#c9d9e9 45%,#8fb0cf)"></div>
  <div class="footer" style="top:209px;height:30px">
    <div class="url">http://www.<b>quorvian</b>.example</div>
    <div class="brand" style="width:98px"><i></i>Quorvian</div>
  </div>
</section>

<section class="slide maps">
  <svg class="badge" style="left:9px" viewBox="0 0 46 62" aria-hidden="true">
    <path d="M0 0H46V62L23 48L0 62Z" fill="var(--orange)"/>
    <text x="23" y="34" font-size="28" text-anchor="middle">4</text>
  </svg>
  <h2 class="heading" style="left:58px;top:17px"><span class="accent" style="font-size:15px">WIFI Network</span><span class="main" style="font-size:15px;margin-top:6px">Management : Maps and Topology</span></h2>
  <ul class="bullets notes" style="left:24px;width:180px"><li>Provides multiple layers of maps in campus, building and floor</li></ul>
  <div class="divider"></div>
  <ul class="bullets notes" style="left:251px;width:190px"><li>Provides tooltips on information for AC, AP and clients summary info in each map</li></ul>
  <div class="visual" role="img" aria-label="Campus map, floor list and access point heat map screenshots"
       style="left:6px;top:96px;width:438px;height:121px;border:3px solid #333;background:linear-gradient(90deg,#7fbf7a 0,#e0e6da 26%,#f7f7f7 27%,#f7f7f7 62%,#9bb8d6 63%,#e6a84a 80%,#8fb0cf 100%)"></div>
  <div class="footer" style="top:220px;height:31px">
    <div class="url">http://www.<b>quorvian</b>.example</div>
    <div class="brand" style="width:98px"><i></i>Quorvian</div>
  </div>
</section>

</body>
</html>
```